【 概要 】 片付けコンサルのサイトのメインバナーのデザイン作成をお願いします。 【 依頼内容 】 ・サイズ: 横2300 × 縦1200px ・作成数: 1種類 【 デザインイメージ 】 ・ターゲット層:40代50代の片付けレッスン検討者層 ・雰囲気:洗練されたきれい目な雰囲気 【 使用素材 】 (使用テキスト) 3ヶ月間で心地よい暮らしをと人生を手に入れる! 片付け本 累計15万部のベストセラー著者が直接レッスン指導 (使用画像) 提供する添付画像から1枚~2枚使って作成ください。 ------------------- |
| https://www.lumo-vista.com | ||
デザインが、想像していたイメージと一致したため。
皆さま、たくさんのご提案をいただきまして、ありがとうございました。どれも、魅力的なご提案で、どのデザインにしようかと非常に悩みました。また、機会がございましたら、依頼をさせていただきたいと思いますので、よろしくお願いいたします。

```html
<!DOCTYPE html>
<html lang="ja">
<head>
<meta charset="UTF-8">
<title>片付けレッスン メインバナー</title>
<link href="https://fonts.googleapis.com/css2?family=Noto+Sans+JP:wght@500;700;900&display=swap" rel="stylesheet">
<style>
  :root {
    --pink: #e9528e;
    --blue: #2f6fae;
    --ink: #3a3a3a;
    --gold: #c9a645;
    --gold-light: #e6cf86;
    --bg: #ffffff;
    --room-light: #f7f6f4;
    --room-mid: #e9e6e2;
  }
  * { margin: 0; padding: 0; box-sizing: border-box; }
  html, body { width: 1200px; height: 626px; overflow: hidden; background: var(--bg); }
  .banner {
    position: relative;
    width: 1200px;
    height: 626px;
    overflow: hidden;
    background: var(--bg);
    font-family: "Noto Sans JP", sans-serif;
  }
  .banner__photo {
    position: absolute;
    top: 0; right: 0;
    width: 680px;
    height: 626px;
    background:
      linear-gradient(90deg, var(--bg) 0%, rgba(255,255,255,0) 28%),
      radial-gradient(ellipse at 68% 55%, #d9d4cf 0%, var(--room-mid) 30%, var(--room-light) 70%);
  }
  .headline {
    position: absolute;
    left: 70px;
    top: 100px;
    font-weight: 900;
    line-height: 1;
    color: var(--blue);
  }
  .headline__line { display: block; white-space: nowrap; }
  .headline__line + .headline__line { margin-top: 24px; }
  .headline__period {
    font-size: 88px;
    color: var(--pink);
    font-style: italic;
    letter-spacing: -2px;
  }
  .headline__particle {
    font-size: 38px;
    font-weight: 700;
    color: #4a6a8a;
    margin-left: 14px;
  }
  .headline__main { font-size: 78px; letter-spacing: 2px; }
  .headline__accent { font-size: 78px; color: var(--pink); }
  .headline__small { font-size: 46px; font-weight: 700; }
  .headline__tail { font-size: 44px; font-weight: 700; margin-left: 4px; }

  .badge {
    position: absolute;
    left: 70px;
    top: 446px;
    width: 130px;
    height: 130px;
  }
  .badge__text {
    position: absolute;
    inset: 0;
    display: flex;
    flex-direction: column;
    align-items: center;
    justify-content: center;
    color: var(--gold);
    font-weight: 700;
    line-height: 1;
  }
  .badge__label { font-size: 15px; }
  .badge__number { font-size: 52px; font-weight: 900; margin: 2px 0; }
  .badge__unit { font-size: 15px; }

  .credential {
    position: absolute;
    left: 236px;
    top: 452px;
    font-size: 31px;
    font-weight: 700;
    line-height: 44px;
    color: var(--ink);
    letter-spacing: 1px;
  }
  .credential__accent { color: var(--pink); }
</style>
</head>
<body>
  <div class="banner">
    <div class="banner__photo" role="img" aria-label="明るい白い部屋で両手を前に組んで微笑む片付けコンサルタントの女性の写真"></div>

    <h1 class="headline">
      <span class="headline__line"><span class="headline__period">3ヵ月</span><span class="headline__particle">で</span></span>
      <span class="headline__line"><span class="headline__main">心地よい時間</span><span class="headline__small">と</span></span>
      <span class="headline__line"><span class="headline__accent">人生</span><span class="headline__tail">を手に入れる!</span></span>
    </h1>

    <div class="badge">
      <svg width="130" height="130" viewBox="0 0 130 130" aria-hidden="true">
        <circle cx="65" cy="65" r="62" fill="none" stroke="var(--gold-light)" stroke-width="3"/>
        <circle cx="65" cy="65" r="54" fill="none" stroke="var(--gold)" stroke-width="1.5"/>
      </svg>
      <div class="badge__text">
        <span class="badge__label">累計</span>
        <span class="badge__number">15</span>
        <span class="badge__unit">万部</span>
      </div>
    </div>

    <p class="credential">
      片付け本<br>
      <span class="credential__accent">ベストセラー</span>著者が<br>
      <span class="credential__accent">直接</span>レッスン指導
    </p>
  </div>
</body>
</html>
```